**SUPER EASY AND QUICK - 2 LABELS FOR MASON JAR (JAR AND LID LABEL)

This is going to be a super easy project for someone who can think of a quick great idea!!!! We want to pick a winner really quick, so give us all you got.

I included a sample picture to make it real eazy!!!!

We are filling 8 oz mason jars with CARAMEL POPCORN and dropping them as thank you treats!!!! We need a 2 x 4 label for the base of the jar, and also a 2.5 in circle for lid!!!

We want to have a design with a caramel popcorn border, or caramel popcorn pieces on the labels.

We need to incorporate our logo on the labels also.

We also need the words "We Were Just popping By To Say Thanks!!!"

The font should be something bubbly and fun, like popcorn!!! Not just a plain boring font.

Our company colors are silver and chocolate brown, so we need to incorporate the labels to have colors that match that.
I HAVE UPLOADED A LOT OF STUFF TO MAKE IT EAZY!!!

AGAIN.....SUPER EASY, QUICK AND FUN PROJECT!!!! WE WANT TO PICK A WINNER FAST!!!!

Requirements
Must have
• Popcorn images on the label, our logo and also try to use our colors or colors that match our company colors (silver and chocolate brown). I would like to use "caramel popcorn images", as they look better than regular popcorn images.
• Words "We Were Just Popping By To Say THANKS!!!!"
• Fun Looking Fonts that stand out!!!!
• WE WANT COLORFUL!!!
Should not have
• NO PLAIN FONTS

```html
<!DOCTYPE html>
<html lang="en">
<head>
<meta charset="utf-8">
<title>Popping By Thank-You Labels</title>
<link rel="stylesheet" href="https://fonts.googleapis.com/css2?family=Lobster&display=swap">
<style>
  :root {
    --chocolate: #7a4a26;
    --chocolate-dark: #5e3518;
    --silver: #9a9a9a;
    --silver-light: #c9c9c9;
    --check: #eeeeee;
    --caramel-light: #e9c48c;
    --caramel: #c98a3e;
    --caramel-dark: #8f5621;
    --paper: #ffffff;
  }
  html, body {
    margin: 0;
    padding: 0;
    width: 1200px;
    height: 900px;
    overflow: hidden;
    background: var(--paper);
  }
  .sheet {
    position: relative;
    width: 1200px;
    height: 900px;
  }
  .sheet svg {
    position: absolute;
    left: 0;
    top: 0;
  }
  .script {
    font-family: "Lobster", cursive;
  }
  .tagline-silver {
    fill: var(--silver);
    stroke: #ffffff;
    stroke-width: 0.6px;
  }
  .tagline-brown {
    fill: var(--chocolate);
    stroke: #ffffff;
    stroke-width: 0.8px;
  }
  .brand-name {
    fill: var(--silver);
  }
</style>
</head>
<body>
<main class="sheet">
  <svg width="1200" height="900" viewBox="0 0 1200 900" xmlns="http://www.w3.org/2000/svg">
    <defs>
      <linearGradient id="caramelFill" x1="0" y1="0" x2="1" y2="1">
        <stop offset="0" stop-color="var(--caramel-light)"/>
        <stop offset="0.5" stop-color="var(--caramel)"/>
        <stop offset="1" stop-color="var(--caramel-dark)"/>
      </linearGradient>
      <radialGradient id="caramelDot" cx="0.45" cy="0.4" r="0.6">
        <stop offset="0" stop-color="var(--caramel-light)"/>
        <stop offset="0.6" stop-color="var(--caramel)"/>
        <stop offset="1" stop-color="var(--caramel-dark)"/>
      </radialGradient>
    </defs>

    <!-- Jar label, landscape 2 x 4 -->
    <g class="jar-label">
      <rect x="63" y="83" width="508" height="253" fill="url(#caramelFill)" role="img" aria-label="Close-up photo of caramel popcorn"/>
      <path d="M63 83 H540 C525 220 380 280 63 300 Z" fill="var(--check)"/>
      <path d="M540 83 C525 220 380 280 63 300" fill="none" stroke="var(--chocolate)" stroke-width="4"/>
      <rect x="78" y="98" width="484" height="230" rx="16" fill="none" stroke="var(--chocolate)" stroke-width="6"/>
      <text class="script tagline-silver" x="95" y="142" font-size="30">We were just</text>
      <text class="script tagline-brown" x="268" y="152" font-size="50">popping</text>
      <text class="script tagline-silver" x="446" y="150" font-size="34">By</text>
      <text class="script tagline-silver" x="160" y="196" font-size="34">to Say</text>
      <text class="script tagline-brown" x="252" y="222" font-size="50">Thanks!!!</text>
      <circle cx="122" cy="234" r="11" fill="var(--silver)"/>
      <text class="script brand-name" x="140" y="242" font-size="22">BrightPath</text>
      <text class="script brand-name" x="142" y="260" font-size="14">Counseling</text>
    </g>

    <!-- Jar label, portrait -->
    <g class="jar-label-tall">
      <rect x="205" y="403" width="224" height="449" fill="var(--chocolate)"/>
      <rect x="217" y="415" width="200" height="425" rx="14" fill="none" stroke="var(--silver-light)" stroke-width="5"/>
      <rect x="229" y="428" width="180" height="400" fill="var(--check)"/>
      <path d="M409 705 V838 H205 V806 C300 800 370 770 409 705 Z" fill="url(#caramelFill)" role="img" aria-label="Photo of caramel popcorn"/>
      <circle cx="263" cy="555" r="28" fill="url(#caramelDot)" role="img" aria-label="Caramel popcorn piece"/>
      <circle cx="336" cy="665" r="28" fill="url(#caramelDot)" role="img" aria-label="Caramel popcorn piece"/>
      <text class="script tagline-silver" x="240" y="465" font-size="27">We were just</text>
      <text class="script tagline-brown" x="250" y="505" font-size="42">popping</text>
      <text class="script tagline-silver" x="310" y="540" font-size="28">By</text>
      <text class="script tagline-silver" x="300" y="585" font-size="28">to Say</text>
      <text class="script tagline-brown" x="232" y="630" font-size="44">Thanks!!!</text>
      <circle cx="250" cy="720" r="10" fill="var(--silver)"/>
      <text class="script brand-name" x="266" y="728" font-size="20">BrightPath</text>
      <text class="script brand-name" x="266" y="750" font-size="15">Counseling</text>
    </g>

    <!-- Lid label, round 2.5 in -->
    <g class="lid-label">
      <circle cx="1033" cy="403" r="145" fill="var(--check)" stroke="var(--chocolate)" stroke-width="5"/>
      <circle cx="942" cy="430" r="30" fill="url(#caramelDot)" role="img" aria-label="Caramel popcorn piece"/>
      <circle cx="1114" cy="479" r="27" fill="url(#caramelDot)" role="img" aria-label="Caramel popcorn piece"/>
      <text class="script tagline-silver" x="955" y="320" font-size="28">We were just</text>
      <text class="script tagline-brown" x="930" y="365" font-size="46">popping</text>
      <text class="script tagline-silver" x="1093" y="362" font-size="32">By</text>
      <text class="script tagline-silver" x="950" y="398" font-size="30">to Say</text>
      <text class="script tagline-brown" x="980" y="434" font-size="42">Thanks!!!</text>
      <circle cx="974" cy="470" r="10" fill="var(--silver)"/>
      <text class="script brand-name" x="990" y="477" font-size="19">BrightPath</text>
      <text class="script brand-name" x="992" y="497" font-size="15">Counseling</text>
    </g>
  </svg>
</main>
</body>
</html>
```